Maple Ridge business card design

Card needs to include the following text/items:
Company Logo
Tobin Marsh
Phone # - 555-318-7642
service@mapleridgelandscaping.example
Lawn & landscape maintenance services

```html
<!DOCTYPE html>
<html lang="en">
<head>
<meta charset="utf-8">
<title>Maple Ridge Landscaping – Business Card</title>
<link rel="stylesheet" href="https://fonts.googleapis.com/css2?family=Cinzel:wght@700&family=EB+Garamond:ital,wght@0,400;1,400&display=swap">
<style>
  :root {
    --backdrop: #3a3a3a;
    --card: #ffffff;
    --card-shade: #ececec;
    --soil: #6b3a1e;
    --forest: #1f4d2b;
    --leaf: #2f6b35;
    --olive: #7a8f2a;
    --gold: #f0c47a;
    --ink: #3b3b3b;
  }
  * { box-sizing: border-box; margin: 0; padding: 0; }
  html, body {
    width: 1200px; height: 900px; overflow: hidden;
    background: var(--backdrop);
  }
  .canvas { position: relative; width: 1200px; height: 900px; }

  .card {
    position: absolute;
    width: 620px; height: 354px;
    background: linear-gradient(135deg, var(--card) 40%, var(--card-shade));
    box-shadow: 0 14px 30px rgba(0,0,0,.45);
    overflow: hidden;
  }
  .card--front { left: 150px; top: 50px; }
  .card--back  { left: 430px; top: 480px; }

  .soil-band {
    position: absolute; left: 0; right: 0; bottom: 0; height: 22px;
    background: var(--soil);
  }

  .tree-art {
    position: absolute;
    background: linear-gradient(180deg, var(--leaf), var(--forest));
  }
  .card--front .tree-art { left: 440px; top: 26px; width: 160px; height: 306px; }
  .card--back  .tree-art { left: 40px;  top: 100px; width: 190px; height: 232px; }

  .brand {
    position: absolute;
    display: flex; flex-direction: column; align-items: center; gap: 8px;
  }
  .brand__mark {
    width: 76px; height: 76px; border-radius: 50%;
    border: 3px solid var(--olive);
    flex: none;
  }
  .brand__name {
    font-family: "Cinzel", serif; font-weight: 700;
    font-size: 32px; color: var(--forest); letter-spacing: .5px;
    white-space: nowrap; line-height: 1.1;
  }
  .card--front .brand { left: 44px; top: 128px; }
  .card--back  .brand { right: 34px; top: 24px; }

  .contact { position: absolute; left: 262px; top: 168px; width: 330px; }
  .contact__name {
    font-family: "Cinzel", serif; font-weight: 700;
    font-size: 26px; color: var(--forest); letter-spacing: 1px;
    margin-bottom: 10px;
  }
  .contact__line {
    display: flex; align-items: center; gap: 10px;
    font-family: "EB Garamond", serif; font-size: 18px; color: var(--ink);
    margin-bottom: 4px; white-space: nowrap;
  }
  .contact__icon { width: 16px; height: 16px; flex: none; }
  .contact__rule {
    height: 2px; background: var(--gold);
    margin: 8px 0 6px;
  }
  .contact__tagline {
    font-family: "EB Garamond", serif; font-style: italic;
    font-size: 21px; color: var(--olive); white-space: nowrap;
  }
</style>
</head>
<body>
<main class="canvas">

  <section class="card card--front">
    <div class="brand">
      <span class="brand__mark"></span>
      <span class="brand__name">Maple Ridge</span>
    </div>
    <div class="tree-art" role="img" aria-label="Illustration area: tall green cedar tree with brown trunk"></div>
    <div class="soil-band"></div>
  </section>

  <section class="card card--back">
    <div class="brand">
      <span class="brand__mark"></span>
      <span class="brand__name">Maple Ridge</span>
    </div>
    <div class="tree-art" role="img" aria-label="Illustration area: tall green cedar tree with brown trunk"></div>

    <div class="contact">
      <p class="contact__name">TOBIN MARSH</p>
      <p class="contact__line">
        <svg class="contact__icon" viewBox="0 0 16 16" aria-hidden="true">
          <path d="M3 2h3l1.5 3.5-2 1.2a8 8 0 0 0 3.8 3.8l1.2-2L14 10v3a1 1 0 0 1-1 1A11 11 0 0 1 2 3a1 1 0 0 1 1-1z" fill="var(--olive)"/>
        </svg>
        555-318-7642
      </p>
      <p class="contact__line">
        <svg class="contact__icon" viewBox="0 0 16 16" aria-hidden="true">
          <rect x="1" y="3" width="14" height="10" rx="1.5" fill="var(--olive)"/>
          <path d="M2 4.5l6 4.5 6-4.5" fill="none" stroke="#fff" stroke-width="1.3"/>
        </svg>
        service@mapleridgelandscaping.example
      </p>
      <div class="contact__rule"></div>
      <p class="contact__tagline">Lawn &amp; landscape maintenance services</p>
    </div>

    <div class="soil-band"></div>
  </section>

</main>
</body>
</html>
```